High End Notary Service Business Card Design

Want a professional and elegant/luxurious business card that is clean and simple in the design. A notary is a trusted professional that helps people sign very important documents. The card should be in alignment with this service provided.

Most of the time, service will be for the purchase of a home or refinance of a mortgage

There is NO LOGO. This is aesthetic. A look and feel. Conveying professionalism and concierge level of service.

Target Market(s)

Other business professionals, Lawyers, Escrow Officers, Loan Officers

Industry/Entity Type

Legal

Contact Information for Business Card

This will be a one-sided business card

Colors
35a7d7
3176b5
85cae6
d3a5cc
b868aa
ffffff
0356a4

Requirements
Must have
• Doreen L. Marsh-Whitlock
Notary Public

614-872-3916
MarshPublicNotary@Vornmail.com
Nice to have
• Headshot photo below. Convey the aspect of signing documents. No black cards. Preference is shades of blue: light blue, navy, aqua, gold, white, or lavendar, etc.
Should not have
• No scales or legal scales.

```html
<!DOCTYPE html>
<html lang="en">
<head>
<meta charset="utf-8">
<title>Doreen L. Marsh-Whitlock — Notary Public Business Card</title>
<link href="https://fonts.googleapis.com/css2?family=Roboto:wght@400;700&display=swap" rel="stylesheet">
<style>
  :root {
    --stage: #161718;
    --card-top: #2e2f31;
    --card-bottom: #242527;
    --accent-blue: #35a7d7;
    --text-white: #ffffff;
    --emboss-text: #2a2b2d;
    --emboss-light: rgba(255,255,255,0.14);
    --emboss-dark: rgba(0,0,0,0.55);
  }
  * { margin: 0; padding: 0; box-sizing: border-box; }
  html, body {
    width: 1200px; height: 900px; overflow: hidden;
    background: var(--stage);
    font-family: "Roboto", Arial, sans-serif;
  }
  .stage {
    width: 1200px; height: 900px;
    display: flex; flex-direction: column;
    align-items: center; justify-content: center; gap: 40px;
  }
  .card {
    position: relative;
    width: 665px; height: 380px;
    background: linear-gradient(160deg, var(--card-top), var(--card-bottom));
    box-shadow: 0 12px 30px rgba(0,0,0,0.55);
  }
  .card-front .holder-name {
    position: absolute; left: 44px; top: 40px;
    font-weight: 700; font-size: 31px; letter-spacing: 0.3px;
    color: var(--accent-blue);
  }
  .card-front .holder-title {
    position: absolute; left: 44px; top: 82px;
    font-weight: 400; font-size: 16px;
    color: var(--text-white);
  }
  .card-front .title-rule {
    position: absolute; left: 32px; top: 110px;
    width: 46px; height: 2px;
    background: var(--text-white);
  }
  .contact-list {
    position: absolute; left: 40px; bottom: 42px;
    list-style: none;
    display: flex; flex-direction: column; gap: 8px;
  }
  .contact-item {
    display: flex; align-items: center; gap: 10px;
    font-size: 15px; color: var(--text-white);
  }
  .contact-icon { width: 14px; height: 14px; flex: none; }
  .card-back .embossed-name {
    position: absolute; left: 0; right: 0; top: 150px;
    text-align: center;
    font-weight: 700; font-size: 38px; letter-spacing: 0.5px;
    color: var(--emboss-text);
    text-shadow: -1px -1px 1px var(--emboss-dark), 1px 1px 1px var(--emboss-light);
  }
</style>
</head>
<body>
<main class="stage">
  <section class="card card-front" aria-label="Business card front">
    <h1 class="holder-name">Doreen L. Marsh-Whitlock</h1>
    <p class="holder-title">Notary Public</p>
    <div class="title-rule"></div>
    <ul class="contact-list">
      <li class="contact-item">
        <svg class="contact-icon" viewBox="0 0 14 14" aria-hidden="true">
          <rect x="3.5" y="1" width="7" height="12" rx="1.2" fill="none" stroke="#35a7d7" stroke-width="1.4"/>
          <line x1="6" y1="11" x2="8" y2="11" stroke="#35a7d7" stroke-width="1.2"/>
        </svg>
        <span>614-872-3916</span>
      </li>
      <li class="contact-item">
        <svg class="contact-icon" viewBox="0 0 14 14" aria-hidden="true">
          <rect x="1" y="3" width="12" height="8.5" fill="#35a7d7"/>
          <polyline points="1,3 7,8 13,3" fill="none" stroke="#242527" stroke-width="1.2"/>
        </svg>
        <span>MarshPublicNotary@Vornmail.com</span>
      </li>
    </ul>
  </section>

  <section class="card card-back" aria-label="Business card back">
    <p class="embossed-name">Doreen L. Marsh-Whitlock</p>
  </section>
</main>
</body>
</html>
```